AUDITING SERVICES FOR IMPORT/EXPORT/LOGISTICS

* PROCUREMENT OF PARTS / SERVICES
* BOAT POSITIONING

Industry/Entity Type

Auditing

Contact Information for Business Card

KTF CONSULTANTS
(WILLOW HARBOUR CRAFT PTY LTD) 17 THE ESPLANADE CORELLA SHORES
DAVID FENWICK 0418274603 LOUISE-JANE FENWICK 0418274681 (ON OPPOSITE SIDE)

```html
<!DOCTYPE html>
<html lang="en">
<head>
<meta charset="utf-8">
<title>KTF Consultants – Willow Harbour Craft Pty Ltd – Business Card</title>
<link rel="stylesheet" href="https://fonts.googleapis.com/css2?family=Tinos&family=Noto+Sans&display=swap">
<style>
  :root {
    --sky-top: #24a9e4;
    --sky-bottom: #0f8ccb;
    --band-top: #3a3a3a;
    --band-black: #000000;
    --sea-top: #0070ad;
    --sea-bottom: #00457c;
    --ink: #ffffff;
  }
  * { margin: 0; padding: 0; box-sizing: border-box; }
  html, body { width: 1200px; height: 741px; overflow: hidden; background: #ffffff; }
  .card {
    position: relative;
    width: 1200px;
    height: 741px;
    overflow: hidden;
    color: var(--ink);
    font-family: "Noto Sans", sans-serif;
  }
  .sky {
    position: absolute; left: 0; top: 0; width: 100%; height: 233px;
    background: linear-gradient(to bottom, var(--sky-top), var(--sky-bottom));
  }
  .name-band {
    position: absolute; left: 0; top: 233px; width: 100%; height: 186px;
    background: linear-gradient(to bottom, var(--band-top) 0%, #151515 22%, var(--band-black) 45%);
  }
  .trading-name {
    position: absolute; left: 0; top: 252px; width: 100%;
    text-align: center;
    font-family: "Tinos", serif;
    font-size: 34px;
    line-height: 44px;
    font-weight: 400;
  }
  .company {
    position: absolute; left: 0; top: 304px; width: 100%;
    text-align: center;
    font-family: "Tinos", serif;
    font-size: 52px;
    line-height: 64px;
    font-weight: 400;
  }
  .sea {
    position: absolute; left: 0; top: 419px; width: 100%; height: 322px;
    background: linear-gradient(to bottom, var(--sea-top), var(--sea-bottom));
  }
  .services {
    position: absolute; left: 0; top: 433px; width: 100%;
    text-align: center;
    font-size: 31px;
    line-height: 43px;
  }
  .contact {
    position: absolute; top: 520px;
    font-size: 29px;
    line-height: 41px;
  }
  .contact--left { left: 56px; text-align: left; }
  .contact--right { right: 56px; text-align: right; }
  .address {
    position: absolute; left: 0; top: 654px; width: 100%;
    text-align: center;
    font-size: 28px;
    line-height: 38px;
  }
</style>
</head>
<body>
  <div class="card">
    <div class="sky"></div>
    <div class="name-band"></div>
    <p class="trading-name">KTF Consultants</p>
    <h1 class="company">Willow Harbour Craft Pty Ltd</h1>
    <div class="sea"></div>
    <div class="services">
      <p>Auditing Services for Import/Export/Logistics</p>
      <p>Procurement of Parts &amp; Services Boat Positioning</p>
    </div>
    <div class="contact contact--left">
      <p class="contact__name">David Fenwick</p>
      <p class="contact__phone">Tel : 61 418 274 603</p>
      <p class="contact__email">david@willowharbourcraft.com</p>
    </div>
    <div class="contact contact--right">
      <p class="contact__name">Louise-Jane Fenwick</p>
      <p class="contact__phone">Tel : 61 418 274 681</p>
      <p class="contact__email">louisejane@willowharbourcraft.com</p>
    </div>
    <p class="address">17 The Esplanade Corella Shores Qld 4517</p>
  </div>
</body>
</html>
```